minimalist website update needed, have wireframes

*Please start by making a design of the My Accounts page. If the overall template is correct, we can expand from there. Will give fast feedback.*

Financial services company (think online banking) is doing a complete website overhaul. We are going for the easiest, simplest possible user experience. We have the entire site mocked up in wireframes, but need a designer to make the final design drafts using photoshop or similar, then it needs to be coded into HTML/CSS.

*Current website*
https://venlotrix.com/

*New website*
+ minimalist
+ white label of https://dubrapurse.org
+ skinning dubrapurse to be Venlotrix branded, and targeted at beginners
+ wireframes for customized pages are attached
+ Landing page design is open. Please suggest one for bonus points!

Notes on the wireframes:
Open to rearranging the header content and menus.
Footer content is very rough. Just need to have a nice placeholder.
Needs social media icons
Needs language selector
My Accounts content is very rough. We want to use this area as a modular dashboard.
App Store is really just links to Bitcoin websites. These help users find useful and fun places to spend their money.

*Branding?*
As part of the process, our branding may need an update. Orange is currently our primary color, and it doesn't match well with the new, simplistic layout. We're willing to explore changes to the brand, if it works better with the new design.

Current visual identity guide is attached.
Updates

Project Deadline Extended
Reason: It seems for this many pages, it is better to leave more time. First we have to get the template right, then content elements, then HTML/CSS. I underestimated the complexity, forgive me for the modification.

Target Market(s)

People who make online purchases, or send money online.

Industry/Entity Type

Financial

Coding

Coded - Design and coding required

Number of Pages Required

5+ page

Requirements
Must have
• Pretty versions of the attached wireframes in HTML
Nice to have
• Landing page

```html
<!DOCTYPE html>
<html lang="en">
<head>
<meta charset="utf-8">
<title>Venlotrix – Add Account</title>
<link href="https://fonts.googleapis.com/css2?family=Josefin+Sans:wght@400;600;700&family=Lato:wght@400;700&display=swap" rel="stylesheet">
<style>
:root{
  --orange:#e2783b;
  --orange-dark:#c3602b;
  --green:#82b69a;
  --green-dark:#6fa488;
  --beige:#f7f6f0;
  --sidebar:#fbf7e8;
  --nav-item:#f5f3ec;
  --grey:#cfcdbd;
  --text:#8a897f;
  --muted:#a9a89d;
  --white:#ffffff;
}
*{margin:0;padding:0;box-sizing:border-box}
html,body{width:1200px;height:771px;overflow:hidden;background:var(--white)}
body{position:relative;font-family:"Lato",sans-serif;color:var(--text)}
.abs{position:absolute}
.label{font-family:"Josefin Sans",sans-serif;letter-spacing:.12em;text-transform:uppercase}

/* sidebar */
.sidebar{left:0;top:0;width:300px;height:771px;background:var(--sidebar)}
.brand{left:0;top:150px;width:300px;text-align:center}
.brand-mark{display:block;margin:0 auto 10px;width:46px;height:46px;border-radius:50%;background:var(--green);margin-top:-80px;margin-bottom:44px}
.brand-name{font-family:"Josefin Sans",sans-serif;font-weight:700;font-size:25px;letter-spacing:.3em;color:var(--orange);padding-left:.3em}
.brand-tag{font-family:"Josefin Sans",sans-serif;font-weight:600;font-size:8.5px;letter-spacing:.14em;color:var(--orange);margin-top:10px}
.side-nav{left:0;top:231px;width:300px;list-style:none}
.side-nav li{height:55.6px;line-height:57px;padding-left:44px;font-size:12px;color:var(--green);background:var(--nav-item);border-bottom:1px solid #ece9df;font-weight:600}
.side-nav li.active{background:var(--orange);color:var(--white)}
.side-social{left:73px;top:627px;display:flex;gap:14px}
.side-social span{width:28px;height:28px;border-radius:50%;background:var(--muted);display:block}
.copyright{left:0;top:674px;width:300px;text-align:center;font-family:"Josefin Sans",sans-serif;font-size:10.5px;letter-spacing:.04em;color:var(--text)}
.copyright a{color:var(--green);text-decoration:none}
.legal{left:0;top:698px;width:300px;text-align:center;font-family:"Josefin Sans",sans-serif;font-size:8.5px;color:var(--text)}

/* header */
.field{height:33px;background:var(--beige);font-size:8.5px;line-height:34px;padding-left:11px;color:var(--text)}
.field .chev{position:absolute;right:12px;top:8px;width:17px;height:17px;border-radius:50%;background:#dad8cb}
.field .chev svg{display:block;margin:5px auto}
.email{left:605px;top:30px;width:145px}
.balance{left:767px;top:30px;width:117px;font-weight:700;font-size:9px}
.lang{left:901px;top:30px;width:120px;padding-left:35px;font-family:"Josefin Sans",sans-serif;font-weight:600;font-size:11px;color:var(--green)}
.lang .flag{position:absolute;left:8px;top:8px;width:18px;height:18px;border-radius:50%;background:#8fa3c6}
.avatar{left:1050px;top:23px;width:46px;height:46px;border-radius:50%;background:radial-gradient(circle at 50% 45%,#e9c99a,#c89a5a);border:2px solid var(--green)}
.user{left:1107px;top:34px;font-family:"Josefin Sans",sans-serif;font-size:10.5px;letter-spacing:.06em;font-weight:600}
.user small{display:block;color:var(--green);font-size:9px;letter-spacing:.14em;margin-top:3px}
.top-nav{left:506px;top:100px;display:flex;align-items:center;font-size:10px;letter-spacing:.1em;color:var(--text);white-space:nowrap}
.top-nav span.dot{width:4px;height:4px;border-radius:50%;background:var(--muted);margin:0 25px}
.top-social{top:89px;display:flex;gap:8px;left:1001px}
.top-social span{width:32px;height:32px;background:var(--beige);display:block}

/* band */
.band{left:300px;top:144px;width:900px;height:71px;background:var(--orange)}
.band h1{font-family:"Josefin Sans",sans-serif;font-weight:600;font-size:20px;letter-spacing:.1em;color:var(--white);text-align:center;line-height:74px}
.help{right:48px;top:12px;width:48px;height:48px;border-radius:50%;background:var(--orange-dark);border:1px solid #f0a97c;color:var(--white);font-family:"Josefin Sans",sans-serif;font-weight:700;font-size:19px;text-align:center;line-height:52px}

/* step cards */
.step{top:311px;width:228px;height:228px;background:var(--beige);text-align:center}
.step.green{background:var(--green)}
.step-num{position:absolute;left:71px;top:-42px;width:86px;height:86px;border-radius:50%;background:var(--white);padding:7px}
.step-num span{display:block;width:72px;height:72px;border-radius:50%;background:var(--grey);color:var(--white);font-family:"Josefin Sans",sans-serif;font-size:32px;line-height:80px}
.green .step-num span{background:var(--green)}
.step h2{margin-top:60px;font-family:"Lato",sans-serif;font-weight:400;font-size:12.5px;letter-spacing:.02em;color:#5f5e56}
.green h2{color:var(--white)}
.step p{text-align:left;font-size:11.5px;line-height:16px;padding:0 32px;margin-top:13px;color:#6b6b5e}
.green p{color:#5a7a66}
.green p a{color:var(--orange)}
.dropdown{position:absolute;left:30px;top:172px;width:168px;height:38px;background:var(--orange);color:var(--white);text-align:left;padding-left:14px;line-height:40px;font-size:11.5px;font-weight:700}
.ring{position:absolute;right:14px;top:10px;width:20px;height:20px;border-radius:50%;border:1px solid var(--white)}
.ring svg{display:block;margin:6px auto}
.assets{position:absolute;left:39px;top:90px;width:150px;list-style:none}
.assets li{height:40px;line-height:42px;background:var(--grey);color:var(--white);text-align:left;padding-left:20px;font-size:11px;font-weight:700;letter-spacing:.08em;position:relative;border-bottom:1px solid #e4e2d6}
.assets li.on{background:var(--green)}
.assets .ring{top:10px;right:17px}
.tick{position:absolute;left:96px;top:94px;width:35px;height:32px;background:var(--green)}
.tick svg{display:block;margin:7px auto}
.step.terms p{position:absolute;left:0;top:146px;margin:0;width:228px;color:#6b6b5e;padding:0 39px}

/* info cards */
.info{top:565px;width:228px;height:146px;background:var(--beige);font-size:11.5px;line-height:16px;padding:21px 32px 0}
.info::before{content:"";position:absolute;left:108px;top:-6px;border:6px solid transparent;border-top:0;border-bottom-color:inherit}
.info.orange{background:var(--orange);color:var(--white);border-color:var(--orange)}
.info.orange a{color:var(--white)}
.info.pale{color:#b9b8ad;border-color:var(--beige)}
.info.pale a{color:#a9a89d;font-weight:700}
.btn{position:absolute;left:68px;top:95px;width:92px;height:33px;line-height:35px;text-align:center;font-size:9.5px;font-weight:700;letter-spacing:.04em;color:var(--white)}
.orange .btn{background:var(--orange-dark)}
.pale .btn{background:#dcdbd0}
.add-btn{left:924px;top:565px;width:228px;height:58px;background:var(--orange);color:var(--white);text-align:center;line-height:62px;font-family:"Josefin Sans",sans-serif;font-weight:600;font-size:14.5px;letter-spacing:.12em}
</style>
</head>
<body>

<aside class="abs sidebar">
  <div class="abs brand">
    <span class="brand-mark"></span>
    <div class="brand-name">VENLOTRIX</div>
    <div class="brand-tag">LAUNCH BITCOINS VIA SMS OR EMAIL</div>
  </div>
  <ul class="abs side-nav label">
    <li class="active">Accounts</li>
    <li>Send</li>
    <li>Fund</li>
    <li>Convert</li>
    <li>History</li>
    <li>Settings</li>
  </ul>
  <div class="abs side-social" aria-label="Social links">
    <span></span><span></span><span></span><span></span>
  </div>
  <div class="abs copyright">© 2015 <a href="https://venlotrix.com/">VENLOTRIX.COM</a> | ALL RIGHTS RESERVED</div>
  <div class="abs legal">PRIVACY POLICY &nbsp;|&nbsp; TERMS</div>
</aside>

<header>
  <div class="abs field email">name@email.com<span class="chev"><svg width="6" height="7" viewBox="0 0 6 7"><path d="M1 1l3 2.5L1 6" stroke="#fff" stroke-width="1.4" fill="none"/></svg></span></div>
  <div class="abs field balance">US $ 11,051.09<span class="chev"><svg width="7" height="6" viewBox="0 0 7 6"><path d="M1 1.5l2.5 3 2.5-3" stroke="#fff" stroke-width="1.4" fill="none"/></svg></span></div>
  <div class="abs field lang"><span class="flag" role="img" aria-label="English flag"></span>EN<span class="chev"><svg width="7" height="6" viewBox="0 0 7 6"><path d="M1 1.5l2.5 3 2.5-3" stroke="#fff" stroke-width="1.4" fill="none"/></svg></span></div>
  <div class="abs avatar" role="img" aria-label="User profile photo"></div>
  <div class="abs user">Hi, Mira<small>LOGOUT</small></div>
  <nav class="abs top-nav label">
    <span>My Wallet</span><span class="dot"></span>
    <span>Store</span><span class="dot"></span>
    <span>About</span><span class="dot"></span>
    <span>Status</span><span class="dot"></span>
    <span>Explorer</span>
  </nav>
  <div class="abs top-social" aria-label="Social links">
    <span></span><span></span><span></span><span></span>
  </div>
</header>

<section class="abs band">
  <h1>ADD ACCOUNT</h1>
  <div class="abs help">?</div>
</section>

<div class="abs step green" style="left:348px">
  <div class="step-num"><span>1</span></div>
  <h2>CHOOSE A CUSTODIAN</h2>
  <p><a href="#">Custodians</a> dolor sit amet, asd consectetuer adipiscing elit,as sed diam nonummy nibh they euismod tincidunt ut laore.....</p>
  <div class="dropdown label">Tetrabond<span class="ring"><svg width="7" height="6" viewBox="0 0 7 6"><path d="M1 1.5l2.5 3 2.5-3" stroke="#fff" stroke-width="1.4" fill="none"/></svg></span></div>
</div>

<div class="abs step" style="left:636px">
  <div class="step-num"><span>2</span></div>
  <h2>CHOOSE AN ASSET</h2>
  <ul class="assets">
    <li class="on">USDV<span class="ring"><svg width="6" height="7" viewBox="0 0 6 7"><path d="M1 1l3 2.5L1 6" stroke="#fff" stroke-width="1.4" fill="none"/></svg></span></li>
    <li>EURV<span class="ring"><svg width="6" height="7" viewBox="0 0 6 7"><path d="M1 1l3 2.5L1 6" stroke="#fff" stroke-width="1.4" fill="none"/></svg></span></li>
    <li>JPYV<span class="ring"><svg width="6" height="7" viewBox="0 0 6 7"><path d="M1 1l3 2.5L1 6" stroke="#fff" stroke-width="1.4" fill="none"/></svg></span></li>
  </ul>
</div>

<div class="abs step terms" style="left:924px">
  <div class="step-num"><span>3</span></div>
  <h2>TERMS OF SPEACH</h2>
  <div class="tick"><svg width="20" height="18" viewBox="0 0 20 18"><path d="M2 9l6 6L18 2" stroke="#fff" stroke-width="2.4" fill="none"/></svg></div>
  <p>i agree from now on that us dollar, $, usd and us$ are all understood to mean usdv.</p>
</div>

<div class="abs info orange" style="left:348px">
  <a href="#">Tetrabond</a> dolor sit amet, asd to a consectetuer adipiscing elit,as sed diam nonummy nibh they euismod tincidunt ut laore.....
  <div class="btn">LEARN MORE</div>
</div>

<div class="abs info pale" style="left:636px">
  USDV dolor sit amet, asd to a consectetuer adipiscing elit,as sed diam nonummy nibh they euismod tincidunt ut <a href="#">Coinmarq</a>.
  <div class="btn">LEARN MORE</div>
</div>

<div class="abs add-btn">ADD ACCOUNT</div>

</body>
</html>
```